Mobile Recording Studio needs business cards

Open to seeing a creative design, but I want to emphasis my logo and minimize the name/title and company information. Possible a fully black background on card.

My company is a mobile sound recording studio. ok to include a my trailer (actual or cartoon) on the card. My initial thought is more straight forward, but a good design will win me over.

SPECS:
CMYK color mode
High (300ppi) raster effect.
cover bleed area
please deliver: Illustrator file with layers and a pdf at completion.

Name and info for the business card:

Dallin Perry
ADR Mixer

email: Dallin@MixVault.com

address:
248 - 5170 East Hollister
Vancouver, BC V5R 2J4

phone:
604.518.2093 office

website:
www.MixVault.com

FB: @MixVault

Instagram: @TheMixVault

Industry/Entity Type

Television Production

Contact Information for Business Card

Dallin Perry
ADR Mixer

email: Dallin@MixVault.com

address:
248 - 5170 East Hollister
Vancouver, BC V5R 2J4

phone:
604.518.2093 office

website:
www.MixVault.com

FB: @MixVault

Instagram: @TheMixVault

Colors

Designer to choose colors to be used in the design.

Requirements
Must have
• emphasis my logo and minimize the name/title and company information.
• SPECS:
• CMYK color mode
• High (300ppi) raster effect.
• cover bleed area
• please deliver: Illustrator file with layers and a pdf at completion.
Nice to have
• maybe include the following:
• all black background or black theme
• my work trailer (actual or cartoon) refer to Instagram: @TheMixVault

```html
<!DOCTYPE html>
<html lang="en">
<head>
<meta charset="utf-8">
<title>The Mix Vault – Business Cards</title>
<link href="https://fonts.googleapis.com/css2?family=Poppins:wght@400;600;800&display=swap" rel="stylesheet">
<style>
  :root {
    --backdrop: #2b2b2c;
    --card-black: #17181a;
    --silver-light: #f4f4f4;
    --silver-mid: #c9c9cb;
    --silver-dark: #8e8f92;
    --logo-silver: #cfd0d2;
    --ink: #111213;
    --ink-soft: #3a3b3d;
  }
  * { margin: 0; padding: 0; box-sizing: border-box; }
  html, body { width: 1200px; height: 960px; overflow: hidden; }
  body {
    background: var(--backdrop);
    font-family: "Poppins", sans-serif;
    position: relative;
  }
  .card {
    position: absolute;
    left: 250px;
    width: 700px;
    height: 400px;
    border-radius: 28px;
    background: var(--card-black);
    overflow: hidden;
    box-shadow: 0 18px 40px rgba(0,0,0,0.55);
  }
  .card--front { top: 50px; }
  .card--back { top: 500px; }

  .brand {
    position: absolute;
    display: flex;
    align-items: center;
    gap: 16px;
    color: var(--logo-silver);
    font-weight: 600;
    letter-spacing: 4px;
    text-transform: uppercase;
    white-space: nowrap;
  }
  .brand__mark {
    width: 18px; height: 18px;
    background: var(--logo-silver);
  }
  .card--front .brand {
    font-size: 52px;
    left: 50%; top: 50%;
    transform: translate(-50%, -50%);
  }
  .card--back .brand {
    font-size: 42px;
    left: 42%; top: 100px;
    transform: translate(-50%, -50%);
  }

  .silver-rule {
    position: absolute;
    left: 0; right: 0;
    top: 196px;
    height: 5px;
    background: linear-gradient(90deg, var(--silver-dark), var(--silver-light) 50%, var(--silver-dark));
  }
  .silver-band {
    position: absolute;
    left: 0; right: 0; bottom: 0;
    top: 208px;
    background: linear-gradient(100deg, var(--silver-dark) 0%, var(--silver-light) 35%, var(--silver-mid) 65%, var(--silver-light) 85%, var(--silver-dark) 100%);
  }

  .person {
    position: absolute;
    left: 60px; top: 272px;
    text-align: right;
    width: 260px;
  }
  .person__name {
    font-weight: 800;
    font-size: 28px;
    color: var(--ink);
    letter-spacing: 0.5px;
  }
  .person__role {
    font-size: 15px;
    color: var(--ink-soft);
    margin-top: 2px;
  }
  .divider {
    position: absolute;
    left: 348px; top: 240px;
    width: 2px; height: 130px;
    background: var(--ink);
  }
  .contact {
    position: absolute;
    left: 372px; top: 236px;
    list-style: none;
    font-size: 15px;
    color: var(--ink-soft);
    line-height: 1.45;
  }
  .contact li { display: flex; align-items: flex-start; gap: 10px; }
  .contact svg { flex: none; margin-top: 4px; }
  .contact .dot {
    flex: none; width: 13px; height: 13px; border-radius: 50%;
    background: var(--ink); margin-top: 5px;
  }
</style>
</head>
<body>

<section class="card card--front" aria-label="Card front">
  <div class="brand"><span class="brand__mark"></span>The Mix Vault</div>
</section>

<section class="card card--back" aria-label="Card back">
  <div class="brand"><span class="brand__mark"></span>The Mix Vault</div>
  <div class="silver-rule"></div>
  <div class="silver-band"></div>

  <div class="person">
    <p class="person__name">DALLIN PERRY</p>
    <p class="person__role">ADR Mixer</p>
  </div>
  <div class="divider"></div>

  <ul class="contact">
    <li>
      <svg width="13" height="16" viewBox="0 0 13 16" aria-hidden="true"><path d="M6.5 0C3 0 0.5 2.6 0.5 6c0 4.3 6 10 6 10s6-5.7 6-10C12.5 2.6 10 0 6.5 0z" fill="#111213"/><circle cx="6.5" cy="6" r="2.3" fill="#e6e6e6"/></svg>
      <span>248 - 5170 East Hollister<br>Vancouver, BC V5R 2J4</span>
    </li>
    <li>
      <svg width="13" height="14" viewBox="0 0 24 24" aria-hidden="true"><path d="M6.6 10.8a15.1 15.1 0 0 0 6.6 6.6l2.2-2.2a1 1 0 0 1 1-.25 11.4 11.4 0 0 0 3.6.57 1 1 0 0 1 1 1V20a1 1 0 0 1-1 1A17 17 0 0 1 3 4a1 1 0 0 1 1-1h3.5a1 1 0 0 1 1 1c0 1.25.2 2.45.57 3.6a1 1 0 0 1-.25 1z" fill="#111213"/></svg>
      <span>604.518.2093</span>
    </li>
    <li>
      <span class="dot"></span>
      <span>@TheMixVault</span>
    </li>
  </ul>
</section>

</body>
</html>
```